Property Management Company Business Cards

Need business cards for a property management company located in Michigan. We manage houses for clients all over the world. Young and modern company, looking for eye catching design. Please work with the attached logo.

Industry/Entity Type

Property Management

Requirements
Must have
• Need lines for address, telephone number, fax number, web site.

Also lines for name, and job title

```html
<!DOCTYPE html>
<html lang="en">
<head>
<meta charset="utf-8">
<title>Lakeshore Prime Management – Business Cards</title>
<link rel="stylesheet" href="https://fonts.googleapis.com/css2?family=PT+Sans:wght@400;700&family=Open+Sans:wght@400;600&display=swap">
<style>
  :root {
    --bg: #e6e0d6;
    --card-white: #ffffff;
    --brand-blue: #27aae1;
    --brand-dark: #3a3a3c;
    --ink: #3a3a3c;
    --label: #2b2b2b;
    --on-dark: #ffffff;
  }
  * { box-sizing: border-box; margin: 0; padding: 0; }
  html, body { width: 1200px; height: 788px; overflow: hidden; }
  body {
    position: relative;
    background: var(--bg);
    font-family: "Open Sans", Arial, sans-serif;
    color: var(--ink);
  }
  .side-label {
    position: absolute;
    font-family: "Open Sans", Arial, sans-serif;
    font-size: 21px;
    color: var(--label);
    transform: translateX(-50%);
    white-space: nowrap;
  }
  .card {
    position: absolute;
    width: 525px;
    height: 299px;
    border-radius: 22px;
    overflow: hidden;
    box-shadow: 0 3px 10px rgba(0,0,0,0.18);
  }
  .card--white { background: var(--card-white); }
  .card--blue { background: var(--brand-blue); }
  .card--dark { background: var(--brand-dark); }

  /* brand lockup */
  .lockup {
    position: absolute;
    display: flex;
    align-items: center;
    gap: 10px;
  }
  .lockup__dot {
    width: 58px; height: 58px;
    border-radius: 50%;
    background: var(--brand-blue);
    flex: none;
  }
  .lockup__rule {
    width: 2px; height: 64px;
    background: currentColor;
    flex: none;
  }
  .lockup__name {
    font-family: "PT Sans", Arial, sans-serif;
    font-weight: 700;
    line-height: 1;
    white-space: nowrap;
  }
  .lockup__title { display: block; font-size: 35px; letter-spacing: -0.3px; }
  .lockup__sub { display: block; font-size: 13px; letter-spacing: 12.6px; margin-top: 4px; }
  .lockup--dark { color: var(--brand-dark); }
  .lockup--light { color: var(--on-dark); }

  /* front */
  .front__band { position: absolute; left: 0; top: 179px; width: 525px; height: 48px; }
  .front__person {
    position: absolute; left: 41px; top: 186px; color: var(--on-dark);
  }
  .front__person-name { font-size: 16px; line-height: 1.2; }
  .front__person-role { font-size: 12px; line-height: 1.5; }
  .front__online {
    position: absolute; right: 45px; top: 185px;
    text-align: right; color: var(--on-dark);
    font-size: 12px; line-height: 22px;
  }
  .front__online b { font-weight: 600; }
  .front__postal {
    position: absolute; left: 0; right: 0; top: 246px;
    text-align: center; font-size: 13px; line-height: 23px; color: var(--ink);
  }
  .front__postal b { font-weight: 600; }

  .web {
    position: absolute; left: 0; right: 0;
    text-align: center;
    font-size: 15px;
    letter-spacing: 4px;
  }
  .web--dark { color: var(--brand-dark); }
  .web--light { color: var(--on-dark); }

  .emblem {
    position: absolute; left: 0; right: 0; top: 58px;
    display: flex; flex-direction: column; align-items: center; gap: 14px;
  }
  .emblem__dot {
    width: 110px; height: 110px; border-radius: 50%;
    background: var(--brand-dark);
  }
  .emblem__name {
    font-family: "PT Sans", Arial, sans-serif;
    font-weight: 700;
    font-size: 24px;
    color: var(--on-dark);
    letter-spacing: 1px;
  }
</style>
</head>
<body>

  <span class="side-label" style="left:320px; top:32px;">Front</span>
  <span class="side-label" style="left:896px; top:32px;">Back - 1</span>
  <span class="side-label" style="left:324px; top:403px;">Back - 2</span>
  <span class="side-label" style="left:896px; top:403px;">Back - 3</span>

  <!-- Front -->
  <section class="card card--white" style="left:55px; top:78px;">
    <div class="lockup lockup--dark" style="left:77px; top:60px;">
      <span class="lockup__dot"></span>
      <span class="lockup__rule"></span>
      <span class="lockup__name">
        <span class="lockup__title">LAKESHORE PRIME</span>
        <span class="lockup__sub">MANAGEMENT</span>
      </span>
    </div>

    <svg class="front__band" viewBox="0 0 525 48" aria-hidden="true">
      <polygon points="0,0 238,0 188,48 0,48" fill="var(--brand-blue)"/>
      <polygon points="250,0 525,0 525,48 200,48" fill="var(--brand-dark)"/>
    </svg>

    <div class="front__person">
      <div class="front__person-name">Your Name</div>
      <div class="front__person-role">Designation</div>
    </div>
    <div class="front__online">
      <div><b>e</b> : info@website.com</div>
      <div><b>w</b> : www.website.com</div>
    </div>
    <div class="front__postal">
      <div><b>p</b> : 123-123-1234 &nbsp;|&nbsp; <b>f</b> : 123-123-1234</div>
      <div>123 Street, Suite #123, Your City, State 12345</div>
    </div>
  </section>

  <!-- Back 1 -->
  <section class="card card--white" style="left:622px; top:74px;">
    <div class="lockup lockup--dark" style="left:73px; top:117px;">
      <span class="lockup__dot"></span>
      <span class="lockup__rule"></span>
      <span class="lockup__name">
        <span class="lockup__title">LAKESHORE PRIME</span>
        <span class="lockup__sub">MANAGEMENT</span>
      </span>
    </div>
    <div class="web web--dark" style="top:246px;">www.website.com</div>
  </section>

  <!-- Back 2 -->
  <section class="card card--blue" style="left:54px; top:446px;">
    <div class="emblem">
      <span class="emblem__dot"></span>
      <span class="emblem__name">LAKESHORE PRIME</span>
    </div>
    <div class="web web--light" style="top:251px;">www.website.com</div>
  </section>

  <!-- Back 3 -->
  <section class="card card--dark" style="left:622px; top:446px;">
    <div class="lockup lockup--light" style="left:73px; top:107px;">
      <span class="lockup__dot"></span>
      <span class="lockup__rule"></span>
      <span class="lockup__name">
        <span class="lockup__title">LAKESHORE PRIME</span>
        <span class="lockup__sub">MANAGEMENT</span>
      </span>
    </div>
    <div class="web web--light" style="top:251px;">www.website.com</div>
  </section>

</body>
</html>
```